Corvath Partners is a boutique consultancy focused on CXO-level advisory on strategy, operations, and organization in the Consumer Packaged Goods and Retail sector.

Our typical clients are senior level executives (Typically SVP level or higher), who hire us to help solve strategic business challenges. Our consultants are typically charged out at very high rates (Typically $2,000 - $3,000 per day), therefore, our business cards need to convey a high end, classy, yet professional image, consistent with high value strategic consulting.

We would like to see designs and colors that convey excellence, competence, and growth.

Our name 'Corvath' is derived from the Native American name of Mt. McKinley, the highest peak in North America. We would like to have a logo on our business card, that is simple yet conveys the aspirational nature of what we offer, i.e enabling the achievement of high performance.

Boutique

Corvath Partners, LLC
4718 Brennock Avenue Northwest, Suite 640
Washington, District of Columbia, 20093
United States
Mobile: +1 202 555 0143
elira.voss@corvathpartnersllc.com

```html
<!DOCTYPE html>
<html lang="en">
<head>
<meta charset="utf-8">
<title>Corvath Partners, LLC — Business Card</title>
<link rel="stylesheet" href="https://fonts.googleapis.com/css2?family=Lato:wght@400;700;900&display=swap">
<style>
  :root {
    --backdrop: #e9eaec;
    --card: #ffffff;
    --brand-blue: #0d4c9b;
    --sky-blue: #2a9fd6;
    --ink: #222428;
    --rule: #8a8d92;
    --shadow: rgba(20, 24, 32, 0.18);
  }
  html, body {
    margin: 0;
    padding: 0;
    width: 1200px;
    height: 848px;
    overflow: hidden;
    background: var(--backdrop);
  }
  .canvas {
    position: relative;
    width: 1200px;
    height: 848px;
    display: flex;
    align-items: center;
    justify-content: center;
  }
  .business-card {
    position: relative;
    width: 900px;
    height: 515px;
    background: var(--card);
    border-radius: 34px;
    box-shadow: 0 18px 40px var(--shadow);
    font-family: "Lato", sans-serif;
    color: var(--ink);
  }
  .address {
    position: absolute;
    top: 52px;
    right: 62px;
    margin: 0;
    text-align: right;
    font-size: 17px;
    line-height: 1.3;
    font-style: normal;
    letter-spacing: 0.2px;
  }
  .brand {
    position: absolute;
    left: 150px;
    right: 92px;
    top: 180px;
    display: flex;
    align-items: center;
    gap: 18px;
  }
  .brand-mark {
    width: 26px;
    height: 26px;
    flex: none;
    background: var(--sky-blue);
  }
  .company-name {
    margin: 0;
    font-size: 60px;
    line-height: 1;
    font-weight: 900;
    color: var(--brand-blue);
    letter-spacing: 0.3px;
    white-space: nowrap;
  }
  .rule {
    position: absolute;
    left: 92px;
    right: 92px;
    height: 1px;
    background: var(--rule);
  }
  .rule--top { top: 332px; }
  .rule--bottom { top: 428px; }
  .contact-row {
    position: absolute;
    left: 92px;
    right: 92px;
    top: 332px;
    height: 96px;
    display: flex;
    align-items: center;
    font-size: 19px;
  }
  .contact-item {
    display: flex;
    align-items: center;
    gap: 16px;
  }
  .contact-icon {
    width: 22px;
    height: 22px;
    flex: none;
  }
  .contact-divider {
    width: 1px;
    height: 34px;
    background: var(--rule);
    margin: 0 36px;
  }
</style>
</head>
<body>
<main class="canvas">
  <article class="business-card">
    <address class="address">
      4718 Brennock Avenue Northwest, Suite 640 Washington<br>
      District of Columbia, 20093 United States
    </address>

    <div class="brand">
      <span class="brand-mark" aria-hidden="true"></span>
      <h1 class="company-name">Corvath Partners, LLC</h1>
    </div>

    <div class="rule rule--top"></div>
    <div class="contact-row">
      <div class="contact-item contact-item--email">
        <svg class="contact-icon" viewBox="0 0 22 22" aria-hidden="true">
          <rect width="22" height="22" fill="#0d4c9b"/>
          <path d="M6.5 5.5c.6-.5 1.4-.4 1.8.2l1.2 1.8c.3.5.2 1.1-.2 1.5l-.8.7c.6 1.4 1.7 2.6 3.1 3.3l.7-.8c.4-.4 1-.5 1.5-.2l1.8 1.1c.6.4.7 1.2.3 1.8l-.7.9c-.6.7-1.6 1-2.5.6-3.1-1.2-5.5-3.6-6.7-6.7-.3-.9-.1-1.9.6-2.5z" fill="#fff"/>
        </svg>
        <span>elira.voss@corvathpartnersllc.com</span>
      </div>
      <span class="contact-divider"></span>
      <div class="contact-item contact-item--phone">
        <svg class="contact-icon" viewBox="0 0 22 22" aria-hidden="true">
          <rect width="22" height="22" fill="#0d4c9b"/>
          <rect x="4.5" y="6.5" width="13" height="9" fill="none" stroke="#fff" stroke-width="1.4"/>
          <path d="M4.5 6.5l6.5 5 6.5-5" fill="none" stroke="#fff" stroke-width="1.4"/>
        </svg>
        <span>+1 202 555 0143</span>
      </div>
    </div>
    <div class="rule rule--bottom"></div>
  </article>
</main>
</body>
</html>
```